Logistics Website Design

See website https://kravenfreightglobal.com for theme and color details. Need the site to be re-done and reflect some of the designs shown in this list here: https://pixelvane.com/tags/logistics-company-website

Target Market(s)

Logistics & Transportation

Industry/Entity Type

Logistics and Supply Chain

Coding

Coded - Design and coding required

Number of Pages Required

5+ page

Requirements
Must have
• Colors must match theme of logo. Looking for a sleek, interactive design.

```html
<!DOCTYPE html>
<html lang="en">
<head>
<meta charset="utf-8">
<title>Kraven Freight Global — Logistics</title>
<link href="https://fonts.googleapis.com/css2?family=Barlow+Condensed:wght@600;700;800&family=Poppins:wght@400;500&display=swap" rel="stylesheet">
<style>
:root{
  --orange:#e8622c;
  --orange-soft:#f08a63;
  --ink:#170b07;
  --ink-2:#2a1c17;
  --paper:#ffffff;
  --mist:#f2efee;
  --muted:#4a403c;
  --head:"Barlow Condensed",sans-serif;
  --body:"Poppins",sans-serif;
}
*{box-sizing:border-box;margin:0;padding:0}
html,body{width:1200px;height:3224px;overflow:hidden;background:var(--paper);font-family:var(--body);color:var(--ink)}
.page{position:relative;width:1200px;height:3224px}
.abs{position:absolute}
.h{font-family:var(--head);font-weight:700;text-transform:uppercase;line-height:.95;letter-spacing:-.5px}
.btn{position:absolute;background:var(--orange);color:#fff;font-family:var(--head);font-weight:600;font-size:12px;text-transform:uppercase;display:flex;align-items:center;justify-content:center;border-radius:4px}
.label{font-family:var(--head);font-weight:600;font-size:15px;text-transform:uppercase}
.copy{font-size:10px;line-height:1.45;color:var(--muted)}

/* hero */
.hero{left:12px;top:12px;width:1175px;height:605px;border-radius:22px;overflow:hidden;
  background:linear-gradient(100deg,#3a3c44 0%,#5a5048 35%,#7b4a2c 65%,#2d2522 100%)}
.hero-shade{inset:0;background:linear-gradient(90deg,rgba(20,14,10,.55),rgba(20,14,10,0) 60%)}
.brand{left:112px;top:18px;display:flex;align-items:center;gap:8px}
.brand-dot{width:18px;height:18px;border-radius:50%;background:var(--orange)}
.brand-name{font-family:var(--head);font-weight:700;font-size:22px;color:#fff;text-transform:uppercase}
.nav{left:573px;top:18px;width:487px;height:42px;background:#fff;border-radius:6px;display:flex;align-items:center;padding:0 6px 0 24px;gap:22px;font-family:var(--head);font-weight:600;font-size:11px;text-transform:uppercase}
.nav .on{color:var(--orange)}
.nav .cta{margin-left:auto;background:var(--orange);color:#fff;padding:8px 26px;border-radius:4px}
.hero h1{left:110px;top:215px;color:#fff;font-size:64px}
.hero p{left:112px;top:352px;color:#fff;font-family:var(--head);font-weight:600;font-size:15px;text-transform:uppercase}
.dots{left:562px;top:556px;display:flex;gap:6px}
.dots i{width:11px;height:11px;border-radius:50%;background:#cfc9c6}
.dots i.on{background:#fff}

/* cards */
.tile{top:694px;width:239px;height:290px;border-radius:14px;overflow:hidden}
.tile .t{position:absolute;right:14px;top:20px;text-align:right;color:#fff;font-size:26px}
.tile.a{left:161px;background:linear-gradient(180deg,#4a6f8c,#7a8994 60%,#4c4f54)}
.tile.a .t{right:auto;left:0;width:100%;text-align:center}
.tile.b{left:411px;background:linear-gradient(180deg,#f0a082,#e8622c)}
.arrow{position:absolute;width:40px;height:40px;border-radius:50%;background:#fff;display:flex;align-items:center;justify-content:center}
.tile .arrow{left:18px;bottom:22px}

/* story */
.story{left:12px;top:1088px;width:1175px;height:485px;border-radius:18px;background:var(--mist)}
.photo{border-radius:10px}
.play{display:flex;align-items:center;gap:8px;font-family:var(--head);font-weight:600;font-size:12px;text-transform:uppercase}
.play i{width:34px;height:34px;border-radius:50%;background:var(--ink);display:flex;align-items:center;justify-content:center}

/* services */
.title{width:1200px;text-align:center;font-size:44px}
.svc{top:1737px;width:228px;height:297px;border-radius:12px;background:var(--ink);color:#fff;padding:0 24px}
.svc.hot{background:linear-gradient(180deg,#f08a6a,#e8622c)}
.svc .ico{position:absolute;left:64px;top:20px;width:100px;height:58px;border-radius:6px;background:var(--orange-soft);opacity:.9}
.svc.hot .ico{background:#fff}
.svc h3{position:absolute;left:24px;top:108px;font-size:18px}
.svc p{position:absolute;left:24px;top:165px;width:180px;font-size:9.5px;line-height:1.3;color:#e9dfdb}
.svc .arrow{right:20px;bottom:20px;width:36px;height:36px;background:#3a2e2a}
.svc.hot .arrow{background:#fff}

/* industries */
.ind-photo{left:123px;top:2191px;width:692px;height:310px;border-radius:14px;background:radial-gradient(circle at 40% 50%,#f39a3c 0,#b5561e 18%,#2c4a6a 55%,#10263e 100%)}
.ind{left:832px;width:241px;height:70px;border:1.5px solid var(--ink);border-radius:8px;display:flex;align-items:center;padding:0 16px;gap:14px;font-family:var(--head);font-weight:600;font-size:15px;text-transform:uppercase}
.ind .ic{width:40px;height:40px;border-radius:50%;background:#f5c5b0}
.ind.on{background:var(--ink);color:#fff}
.ind.on .ic{background:#fff}
.ind.on .arrow{position:static;margin-left:auto;width:34px;height:34px}

/* footer */
.foot{left:12px;top:2603px;width:1175px;height:607px;border-radius:18px;background:var(--ink);overflow:hidden;color:#fff}
.signup{left:62px;top:52px;font-size:42px}
.field{top:163px;height:48px;border-radius:5px;background:var(--ink-2);color:#e7dcd7;font-size:11px;display:flex;align-items:center;padding-left:16px}
.menu{left:851px;top:0;width:324px;height:607px;border-left:1px solid #3a2e2a}
.menu div{height:101px;border-bottom:1px solid #3a2e2a;display:flex;align-items:center;justify-content:center;font-family:var(--head);font-weight:700;font-size:32px;text-transform:uppercase}
.menu div.on{color:var(--orange)}
.bigname{left:60px;top:430px;font-size:112px;color:#fff}
.connect{left:645px;top:315px}
.connect li{list-style:none;display:flex;align-items:center;gap:14px;font-size:11px;margin-top:14px}
.connect li i{width:30px;height:30px;border-radius:50%;background:#3a2e2a;display:flex;align-items:center;justify-content:center}
.legal{left:520px;top:530px;font-size:10.5px;color:#fff}
</style>
</head>
<body>
<div class="page">

  <section class="abs hero">
    <div class="abs hero-shade" role="img" aria-label="Row of orange and dark freight trucks parked at a loading dock at sunset"></div>
    <div class="abs brand"><span class="brand-dot"></span><span class="brand-name">Kraven Freight</span></div>
    <nav class="abs nav">
      <span class="on">Home</span><span>Services ▾</span><span>Industries ▾</span><span>Request a Quote ▾</span><span>About Us</span>
      <span class="cta">Contact Us</span>
    </nav>
    <h1 class="abs h">Delivering Strength<br>in Every Mile</h1>
    <p class="abs">Secure and reliable transportation for all your cargo needs.</p>
    <div class="btn" style="left:112px;top:396px;width:134px;height:35px">Request a Quote</div>
    <div class="abs dots"><i></i><i class="on"></i><i></i></div>
  </section>

  <div class="abs tile a" role="img" aria-label="Blue freight truck on an open highway">
    <div class="t h">Logistics<br>Worldwide</div>
    <div class="arrow"><svg width="12" height="12" viewBox="0 0 12 12"><path d="M2 10L10 2M4 2h6v6" stroke="#170b07" stroke-width="1.4" fill="none"/></svg></div>
  </div>
  <div class="abs tile b" role="img" aria-label="Orange shipping container lifted by a crane">
    <div class="t h">Continental<br>Ocean Freight</div>
    <div class="arrow"><svg width="12" height="12" viewBox="0 0 12 12"><path d="M2 10L10 2M4 2h6v6" stroke="#170b07" stroke-width="1.4" fill="none"/></svg></div>
  </div>
  <div class="abs label" style="left:710px;top:708px">Logistics Worldwide</div>
  <h2 class="abs h" style="left:710px;top:732px;font-size:44px">Keeping Your Supply<br>Chain Moving</h2>
  <p class="abs copy" style="left:710px;top:828px;width:345px">We deliver a comprehensive range of open-deck and specialized transportation services—including flatbed, step deck, heavy haul, and over-dimensional freight solutions. Backed by years of experience, a trusted nationwide carrier network, and a strong safety-first culture, we provide reliable, adaptable logistics support built around the unique requirements of every load.</p>
  <div class="btn" style="left:712px;top:938px;width:134px;height:34px">Request a Quote</div>

  <section class="abs story"></section>
  <div class="abs label" style="left:160px;top:1198px">Our Story</div>
  <h2 class="abs h" style="left:160px;top:1222px;font-size:44px">Driven by Logistics.<br>Powered by Trust.</h2>
  <p class="abs copy" style="left:160px;top:1320px;width:350px">Kraven Freight Global™ was born out of real-world experience in the fitness equipment industry. What started as a company shipping strength equipment, cardio machines, and training gear to gyms, schools, and commercial facilities quickly evolved into something bigger. As order volume grew and supply chains became more complex, the team developed deep expertise...</p>
  <div class="btn" style="left:163px;top:1428px;width:134px;height:36px">Learn More</div>
  <div class="abs play" style="left:322px;top:1430px"><i><svg width="8" height="8" viewBox="0 0 8 8"><path d="M1 0l7 4-7 4z" fill="#fff"/></svg></i>Watch Video</div>
  <div class="abs photo" style="left:627px;top:1163px;width:409px;height:337px;background:linear-gradient(160deg,#d49a6a,#9b3a2c 55%,#5a3a24)" role="img" aria-label="Red semi truck on a desert road at sunset"></div>
  <div class="abs photo" style="left:565px;top:1288px;width:135px;height:174px;border:3px solid #fff;background:linear-gradient(160deg,#8fa2b5,#1e2228 70%)" role="img" aria-label="Black semi truck parked outdoors"></div>

  <h2 class="abs h title" style="top:1668px">Our Services</h2>
  <div class="abs svc" style="left:125px"><div class="ico" role="img" aria-label="Flatbed truck icon"></div><h3 class="h">Flatbed<br>Transportation</h3><p>From routine shipments to oversized and heavy-haul loads, we handle freight requiring proper securement, regulatory knowledge, and consistent on-time execution.</p><div class="arrow"><svg width="12" height="12" viewBox="0 0 12 12"><path d="M2 10L10 2M4 2h6v6" stroke="#fff" stroke-width="1.4" fill="none"/></svg></div></div>
  <div class="abs svc hot" style="left:365px"><div class="ico" role="img" aria-label="Step deck truck icon"></div><h3 class="h">Step Deck<br>Transportation</h3><p>Our step deck trucking services support tall, heavy, and specialized freight that requires additional height clearance and flexible loading options.</p><div class="arrow"><svg width="12" height="12" viewBox="0 0 12 12"><path d="M2 10L10 2M4 2h6v6" stroke="#170b07" stroke-width="1.4" fill="none"/></svg></div></div>
  <div class="abs svc" style="left:605px"><div class="ico" role="img" aria-label="Dry van truck icon"></div><h3 class="h">Dry Van<br>Transportation</h3><p>From consumer goods to industrial materials, our dry van services provide the space, security, and consistency you need coast to coast.</p><div class="arrow"><svg width="12" height="12" viewBox="0 0 12 12"><path d="M2 10L10 2M4 2h6v6" stroke="#fff" stroke-width="1.4" fill="none"/></svg></div></div>
  <div class="abs svc" style="left:845px"><div class="ico" role="img" aria-label="Heavy haul tanker truck icon"></div><h3 class="h">Heavy Haul<br>Transportation</h3><p>We provide heavy haul trucking solutions for oversized, overweight, and over-dimensional freight.</p><div class="arrow"><svg width="12" height="12" viewBox="0 0 12 12"><path d="M2 10L10 2M4 2h6v6" stroke="#fff" stroke-width="1.4" fill="none"/></svg></div></div>

  <h2 class="abs h title" style="top:2119px">Industries</h2>
  <div class="abs ind-photo" role="img" aria-label="Industrial machine drilling metal with glowing sparks on a factory line"></div>
  <div class="abs ind" style="top:2191px"><span class="ic" role="img" aria-label="Food and drink icon"></span>Food &amp; Beverage</div>
  <div class="abs ind on" style="top:2271px"><span class="ic" role="img" aria-label="Gear icon"></span>Manufacturing<span class="arrow"><svg width="12" height="12" viewBox="0 0 12 12"><path d="M2 10L10 2M4 2h6v6" stroke="#170b07" stroke-width="1.4" fill="none"/></svg></span></div>
  <div class="abs ind" style="top:2351px"><span class="ic" role="img" aria-label="Shopping cart icon"></span>E-Commerce &amp; Retail</div>
  <div class="abs ind" style="top:2431px"><span class="ic" role="img" aria-label="Pharmacy icon"></span>Pharma &amp; Healthcare</div>

  <footer class="abs foot">
    <h2 class="abs h signup">Signup to receive our offer,<br>and stay upto date</h2>
    <div class="abs field" style="left:62px;width:270px">Your Name</div>
    <div class="abs field" style="left:343px;width:270px">Email Address</div>
    <div class="btn" style="left:624px;top:163px;width:147px;height:48px">Submit ➤</div>
    <div class="abs h bigname">Kraven</div>
    <div class="abs connect">
      <div class="label">Connect With Us</div>
      <ul>
        <li><i><svg width="12" height="12" viewBox="0 0 12 12"><circle cx="6" cy="6" r="5" stroke="#e8622c" fill="none" stroke-width="1.4"/><path d="M1 6h10M6 1c-2 3-2 7 0 10M6 1c2 3 2 7 0 10" stroke="#e8622c" fill="none"/></svg></i>Website</li>
        <li><i><svg width="12" height="10" viewBox="0 0 12 10"><rect x=".5" y=".5" width="11" height="9" rx="1" fill="#e8622c"/><path d="M1 1l5 4 5-4" stroke="#170b07" fill="none"/></svg></i>Email</li>
        <li><i><svg width="12" height="12" viewBox="0 0 12 12"><path d="M2 1l2.5 0 1 3-1.5 1a7 7 0 003 3l1-1.5 3 1V11a1 1 0 01-1 1A10 10 0 011 2a1 1 0 011-1z" fill="#e8622c"/></svg></i>Phone</li>
      </ul>
    </div>
    <div class="abs legal">© 2026. An independent agent of Halden Crest LLC.</div>
    <nav class="abs menu">
      <div>Home</div><div>Services</div><div>Industries</div><div class="on">Request a Quote</div><div>About Us</div><div style="border-bottom:0">Contact Us</div>
    </nav>
  </footer>

</div>
</body>
</html>
```